PowerPoint Design Project

We need a powerpoint design for our consulting company, Halvern Consulting. We provide technology strategy and solutioning services, with an emphasis on cloud technology. More information about our services can be found at www.halvernconsulting-example.com

We are looking for a design that is professional, but not corporate stuffy. The design needs to use our primary colors in our brand.
Updates

Reason: We need to iterate on some of the great designs, plus, many people have not had a chance to submit their design yet.

Reason: We had a lot of people accept the project, but not all of them have responded yet. We wanted to get them some time, plus, ask a couple of people to make some minor revisions.

Target Market(s)

Technology buyers between the ages of 30-55 at Pinnacle 900 companies

Industry/Entity Type

It Company

Requirements
Must have
• Must follow our logo colors.
Must have at least a cover slide and interior content slide.
Should not have
• Should not contain anything cartoonish or anything with lots of clouds

```html
<!DOCTYPE html>
<html lang="en">
<head>
<meta charset="utf-8">
<title>Halvern Consulting – Presentation Slides</title>
<link href="https://fonts.googleapis.com/css2?family=Source+Sans+3:wght@400;600;700&display=swap" rel="stylesheet">
<style>
:root{
  --blue:#1ba1dc;
  --brown:#7b6e64;
  --rule:#8b8178;
  --ink:#5d5550;
  --page:#e4e4e6;
  --white:#ffffff;
  --bronze:#9d4a22;
  --bronze-2:#c99a80;
  --bronze-3:#e6cdbd;
  --silver:#8a8a8a;
  --silver-2:#bdbdbd;
  --silver-3:#e3e3e3;
  --gold:#c08a35;
  --gold-2:#dcb97c;
  --gold-3:#f0e0c2;
  --blue-2:#8ccbec;
  --blue-3:#cbe8f7;
}
*{box-sizing:border-box;margin:0;padding:0}
html,body{width:771px;height:1200px;overflow:hidden;background:var(--page)}
body{font-family:"Source Sans 3",Arial,sans-serif;color:var(--ink)}
.canvas{position:relative;width:771px;height:1200px;background:var(--page)}
.slide{position:absolute;width:346px;height:260px;background:var(--white);overflow:hidden;box-shadow:0 1px 3px rgba(0,0,0,.18)}
.col-l{left:32px}.col-r{left:393px}
.row-1{top:38px}.row-2{top:327px}.row-3{top:617px}.row-4{top:907px}
.abs{position:absolute}
.slide-title{position:absolute;left:19px;top:13px;font-size:18px;color:var(--blue);font-weight:400}
.title-rule{position:absolute;left:0;top:45px;width:330px;height:1px;background:var(--rule)}
.title-marker{position:absolute;left:19px;top:45px}
.slide-sub{position:absolute;left:19px;top:58px;font-size:10.5px;color:var(--ink)}
.foot-line{position:absolute;left:0;right:0;top:246px;height:1.5px;background:var(--blue)}
.foot-band{position:absolute;left:0;right:0;top:251px;height:9px;background:var(--brown)}
.fine{font-size:4.3px;line-height:5.2px;color:var(--ink)}
.fine p{margin-bottom:3px}
.head-s{font-size:5.5px;font-weight:700;color:var(--blue);margin-bottom:4px}
.bubbles{position:absolute;background:radial-gradient(circle at 70% 40%,rgba(200,190,180,.55),rgba(200,190,180,0) 60%)}
.wordmark{font-weight:400;white-space:nowrap}
/* cover */
.cover-logo{position:absolute;left:82px;top:60px;font-size:26px;color:var(--brown);letter-spacing:-.3px}
.cover-dot{position:absolute;left:64px;top:72px;width:11px;height:11px;border-radius:50%;background:var(--blue)}
.cover-tag{position:absolute;left:197px;top:92px;font-size:7.5px;color:var(--brown)}
.cover-band{position:absolute;left:0;right:0;top:140px;height:11px;background:var(--blue)}
.cover-field{position:absolute;left:0;right:0;top:153px;bottom:0;background:var(--brown)}
.cover-welcome{position:absolute;left:131px;top:178px;font-size:21px;color:var(--blue)}
.cover-lead{position:absolute;left:105px;top:210px;width:180px;font-size:5px;line-height:6px;color:var(--white);text-align:right}
/* profile */
.profile-art{position:absolute;left:0;top:80px;width:105px;height:158px}
.profile-blue{position:absolute;left:0;top:0;width:49px;height:158px;background:linear-gradient(180deg,#3bb1e4,var(--blue))}
.profile-brown{position:absolute;left:49px;top:0;width:56px;height:158px;background:var(--brown)}
.profile-name{position:absolute;left:68px;top:148px;transform:rotate(-90deg);transform-origin:left top;font-size:14px;color:var(--white)}
.profile-text{position:absolute;left:123px;top:85px;width:208px}
/* team */
.member{position:absolute;top:86px;width:80px}
.portrait{width:75px;height:81px;border:1.5px solid var(--brown);background:linear-gradient(180deg,#ffffff,#b9aea5)}
.member-name{font-size:7.5px;font-weight:700;color:var(--blue);margin-top:9px}
.member-role{font-size:3.8px;color:var(--ink);margin-bottom:4px}
/* services */
.service-tile{position:absolute;width:94px;height:73px;border-radius:6px;background:var(--brown);color:var(--white);font-size:9px;line-height:11px;box-shadow:0 1px 2px rgba(0,0,0,.25);overflow:hidden}
.service-tile span{position:absolute;left:36px;top:36px}
.service-tile .bubbles{left:0;top:0;width:40px;height:40px;background:radial-gradient(circle at 30% 30%,rgba(200,190,180,.6),rgba(200,190,180,0) 70%)}
/* plans */
.plans{position:absolute;left:18px;top:77px;border-collapse:collapse;width:309px;font-size:6px;text-align:center}
.plans td,.plans th{height:21px;width:77px;border:1px solid #fff;color:#3e3833;font-weight:400}
.plans th{font-size:10.5px;color:#fff;font-weight:600}
.plans .price td{color:#fff;font-weight:700;font-size:7px}
.c-plan{background:var(--blue)}.c-br{background:var(--bronze)}.c-si{background:var(--silver)}.c-go{background:var(--gold)}
.p2{background:var(--blue-2)}.b2{background:var(--bronze-2)}.s2{background:var(--silver-2)}.g2{background:var(--gold-2)}
.p3{background:var(--blue-3)}.b3{background:var(--bronze-3)}.s3{background:var(--silver-3)}.g3{background:var(--gold-3)}
/* contact */
.contact{background:var(--brown)}
.contact .title-rule{background:var(--blue)}
.contact .slide-sub{color:var(--white)}
.contact-logo{position:absolute;left:28px;top:192px;font-size:12px;color:var(--white)}
.contact-dot{position:absolute;left:17px;top:196px;width:7px;height:7px;border-radius:50%;background:var(--white)}
.contact-web{position:absolute;left:17px;top:212px;width:105px;height:46px;background:var(--blue);color:#fff;font-size:5.8px;font-weight:700;padding:6px 0 0 5px;white-space:nowrap}
.contact-col{position:absolute;font-size:5.8px;line-height:8px;color:var(--white);white-space:nowrap}
.contact-col h4{font-size:5.8px;color:var(--blue);font-weight:700}
.contact-col .blue{color:var(--blue)}
.contact-divider{position:absolute;left:154px;top:210px;width:180px;height:1px;background:rgba(255,255,255,.35)}
</style>
</head>
<body>
<div class="canvas">

  <section class="slide col-l row-1">
    <div class="cover-dot"></div>
    <div class="cover-logo wordmark">Halvern Consulting</div>
    <div class="cover-tag">strategy + cloud + delivery</div>
    <div class="cover-band"></div>
    <div class="cover-field"></div>
    <div class="bubbles" role="img" aria-label="Soft bubble pattern" style="left:180px;top:153px;width:166px;height:107px"></div>
    <div class="cover-welcome">Welcome</div>
    <p class="cover-lead">Strategy and cloud solutions shaped around your business goals.<br>Clear thinking, practical delivery.</p>
  </section>

  <section class="slide col-r row-1">
    <h2 class="slide-title">Company profile</h2>
    <div class="title-rule"></div>
    <svg class="title-marker" width="14" height="8" viewBox="0 0 14 8"><path d="M0 0H14L7 8Z" fill="var(--rule)"/></svg>
    <div class="slide-sub">Who we are</div>
    <div class="profile-art">
      <div class="profile-blue" role="img" aria-label="Blue bubble pattern panel"></div>
      <div class="profile-brown"></div>
      <div class="profile-name wordmark">Halvern Consulting</div>
    </div>
    <div class="profile-text fine">
      <div class="head-s">About Lorem</div>
      <p>We help technology leaders plan, build and run modern platforms. Our team blends business insight with deep cloud experience to deliver change that lasts and scales.</p>
      <p>From first workshop to final rollout, we stay close to your people and your goals.</p>
      <p>Every engagement starts with listening. We map what you have, define where you want to be, and chart a clear route between the two with measurable steps.</p>
      <div class="head-s" style="margin-top:10px">Mision Lorem</div>
      <p>Our mission is to make technology decisions simple, confident and well informed for every client, whatever their size or sector.</p>
      <p>We favour open advice, honest timelines and solutions that fit.</p>
      <p>We measure success by the outcomes our clients reach long after our work is done, and by the trust they place in us again.</p>
    </div>
    <div class="foot-line"></div><div class="foot-band"></div>
  </section>

  <section class="slide col-l row-2">
    <h2 class="slide-title">Meet the team</h2>
    <div class="title-rule"></div>
    <svg class="title-marker" width="14" height="8" viewBox="0 0 14 8"><path d="M0 0H14L7 8Z" fill="var(--rule)"/></svg>
    <div class="slide-sub">Our Creative minds</div>
    <div class="member" style="left:19px">
      <div class="portrait" role="img" aria-label="Team member portrait"></div>
      <div class="member-name">Rowan Ellery</div>
      <div class="member-role">Designation</div>
      <p class="fine">Leads cloud strategy work with a focus on clear roadmaps, steady delivery and strong client partnerships across many sectors.</p>
    </div>
    <div class="member" style="left:135px">
      <div class="portrait" role="img" aria-label="Team member portrait"></div>
      <div class="member-name">Rowan Ellery</div>
      <div class="member-role">Designation</div>
      <p class="fine">Leads cloud strategy work with a focus on clear roadmaps, steady delivery and strong client partnerships across many sectors.</p>
    </div>
    <div class="member" style="left:252px">
      <div class="portrait" role="img" aria-label="Team member portrait"></div>
      <div class="member-name">Rowan Ellery</div>
      <div class="member-role">Designation</div>
      <p class="fine">Leads cloud strategy work with a focus on clear roadmaps, steady delivery and strong client partnerships across many sectors.</p>
    </div>
    <div class="foot-line"></div><div class="foot-band"></div>
  </section>

  <section class="slide col-r row-2">
    <h2 class="slide-title">Our services</h2>
    <div class="title-rule"></div>
    <svg class="title-marker" width="14" height="8" viewBox="0 0 14 8"><path d="M0 0H14L7 8Z" fill="var(--rule)"/></svg>
    <div class="slide-sub">What we do</div>
    <div class="fine abs" style="left:19px;top:77px;width:312px">
      <p>We guide organisations through technology strategy, architecture and delivery, with a strong emphasis on cloud platforms that grow with the business and keep costs clear.</p>
      <p>Our consultants work alongside your teams to shape plans, choose the right tools and bring them to life.</p>
      <p>Each service can stand alone or combine into a full programme, from early assessment through migration, optimisation and ongoing support for your people.</p>
    </div>
    <div class="service-tile" style="left:19px;top:148px"><div class="bubbles" role="img" aria-label="Bubble pattern"></div><span>Services<br>Name 1</span></div>
    <div class="service-tile" style="left:125px;top:148px"><div class="bubbles" role="img" aria-label="Bubble pattern"></div><span>Services<br>Name 2</span></div>
    <div class="service-tile" style="left:230px;top:148px"><div class="bubbles" role="img" aria-label="Bubble pattern"></div><span>Services<br>Name 3</span></div>
    <div class="foot-line"></div><div class="foot-band"></div>
  </section>

  <section class="slide col-l row-3">
    <h2 class="slide-title">Our services</h2>
    <div class="title-rule"></div>
    <svg class="title-marker" width="14" height="8" viewBox="0 0 14 8"><path d="M0 0H14L7 8Z" fill="var(--rule)"/></svg>
    <div class="slide-sub">Services Name</div>
    <div class="service-tile" style="left:17px;top:93px"><div class="bubbles" role="img" aria-label="Bubble pattern"></div><span>Services<br>Name 1</span></div>
    <div class="fine abs" style="left:126px;top:93px;width:202px">
      <div class="head-s">Services Detail</div>
      <p>We assess your current estate, define a target cloud architecture and set out a phased plan with costs, risks and clear milestones for each stage.</p>
      <p>Workshops bring your stakeholders together so every decision is shared and understood.</p>
      <p>Our delivery teams then handle migration, security and governance, keeping services running while new platforms come online smoothly.</p>
      <p>After launch we tune performance and spend, and train your staff to own it.</p>
      <p>Regular reviews keep the platform aligned with changing goals, helping you adopt new capabilities with confidence and at the right pace.</p>
    </div>
    <div class="foot-line"></div><div class="foot-band"></div>
  </section>

  <section class="slide col-r row-3">
    <h2 class="slide-title">Statistics</h2>
    <div class="title-rule"></div>
    <svg class="title-marker" width="14" height="8" viewBox="0 0 14 8"><path d="M0 0H14L7 8Z" fill="var(--rule)"/></svg>
    <div class="slide-sub">Numbers &amp; figures</div>
    <svg class="abs" style="left:12px;top:92px" width="178" height="128" viewBox="0 0 178 128" font-family="Source Sans 3, Arial, sans-serif" font-size="5.5" fill="#333">
      <g stroke="#e2e2e2" stroke-width=".5">
        <path d="M22 4H168M22 14.8H168M22 25.6H168M22 36.4H168M22 47.2H168M22 58H168M22 68.8H168M22 79.6H168M22 90.4H168M22 101.2H168"/>
      </g>
      <path d="M22 4V112H168" stroke="#555" stroke-width=".6" fill="none"/>
      <g text-anchor="end">
        <text x="18" y="114">0</text><text x="18" y="103.2">0.5</text><text x="18" y="92.4">1</text>
        <text x="18" y="81.6">1.5</text><text x="18" y="70.8">2</text><text x="18" y="60">2.5</text>
        <text x="18" y="49.2">3</text><text x="18" y="38.4">3.5</text><text x="18" y="27.6">4</text>
        <text x="18" y="16.8">4.5</text><text x="18" y="6">5</text>
      </g>
      <g fill="var(--blue)">
        <rect x="29" y="19.1" width="10" height="92.9"/><rect x="65.5" y="58" width="10" height="54"/>
        <rect x="102" y="36.4" width="10" height="75.6"/><rect x="138.5" y="14.8" width="10" height="97.2"/>
      </g>
      <g fill="var(--brown)">
        <rect x="39" y="60.2" width="10" height="51.8"/><rect x="75.5" y="17" width="10" height="95"/>
        <rect x="112" y="73.1" width="10" height="38.9"/><rect x="148.5" y="51.5" width="10" height="60.5"/>
      </g>
      <g text-anchor="middle">
        <text x="39" y="122">2010</text><text x="75.5" y="122">2011</text>
        <text x="112" y="122">2012</text><text x="148.5" y="122">2013</text>
      </g>
    </svg>
    <div class="fine abs" style="left:194px;top:93px;width:132px">
      <div class="head-s">Profit and revenue</div>
      <p>Revenue has grown steadily as more clients move core workloads to the cloud with our support and guidance.</p>
      <p>Repeat engagements now make up a large share of our annual project work.</p>
      <p>Margins dipped in one year as we invested in new practice areas and training, then recovered as those teams began delivering for clients across several regions.</p>
      <p>We expect continued growth as demand for cloud strategy rises.</p>
    </div>
    <div class="foot-line"></div><div class="foot-band"></div>
  </section>

  <section class="slide col-l row-4">
    <h2 class="slide-title">Our Plans &amp; pricing</h2>
    <div class="title-rule"></div>
    <svg class="title-marker" width="14" height="8" viewBox="0 0 14 8"><path d="M0 0H14L7 8Z" fill="var(--rule)"/></svg>
    <div class="slide-sub">What we offer</div>
    <table class="plans">
      <tr><th class="c-plan">Plan</th><th class="c-br">Bronze</th><th class="c-si">Siver</th><th class="c-go">Gold</th></tr>
      <tr><td class="p2">Number</td><td class="b2">6/ month</td><td class="s2">24/ month</td><td class="g2">48/ month</td></tr>
      <tr><td class="p3">Traffic</td><td class="b3">2</td><td class="s3">10</td><td class="g3">50</td></tr>
      <tr><td class="p2">Users</td><td class="b2">1 Year</td><td class="s2">5 Year</td><td class="g2">Unlimited</td></tr>
      <tr><td class="p3">Satisfaction</td><td class="b3">Guaranteed</td><td class="s3">Guaranteed</td><td class="g3">Guaranteed</td></tr>
      <tr class="price"><td class="c-plan">Price</td><td class="c-br">$ 38</td><td class="c-si">$ 48</td><td class="c-go">$ 88</td></tr>
    </table>
    <p class="fine abs" style="left:18px;top:211px;width:309px">Every plan includes a dedicated consultant, regular progress reports and access to our cloud specialists. Plans can be upgraded at any time as your needs grow, and custom packages are available for larger programmes across multiple teams or regions.</p>
    <div class="foot-line"></div><div class="foot-band"></div>
  </section>

  <section class="slide col-r row-4 contact">
    <div class="bubbles" role="img" aria-label="Soft bubble pattern" style="left:0;top:0;width:346px;height:110px;background:radial-gradient(circle at 55% 45%,rgba(200,190,180,.45),rgba(200,190,180,0) 65%)"></div>
    <h2 class="slide-title">Send us a message</h2>
    <div class="title-rule"></div>
    <svg class="title-marker" width="14" height="8" viewBox="0 0 14 8"><path d="M0 0H14L7 8Z" fill="var(--blue)"/></svg>
    <div class="slide-sub">Our contact informaton</div>
    <div class="contact-dot"></div>
    <div class="contact-logo wordmark">Halvern Consulting</div>
    <div class="contact-web">www.halvernconsulting-example.com</div>
    <div class="contact-col" style="left:154px;top:150px">
      <h4>Our Address</h4>
      4410 Larkmoor Ave<br>Suite 8<br>Dunmore Falls, Oregon<br>United States
    </div>
    <div class="contact-col" style="left:246px;top:150px">
      <h4>E-mail</h4>
      You can contact us at<br><span class="blue">info@halvern-example.com</span><br>or me directly at<br><span class="blue">hello@halvern-example.com</span>
    </div>
    <div class="contact-divider"></div>
    <div class="contact-col" style="left:154px;top:226px">
      <span class="blue">P:</span> (555) 014-2270<br><span class="blue">F:</span> (555) 019-8834
    </div>
    <div class="contact-col" style="left:246px;top:214px">
      <h4>On the web</h4>
      social.example/halvern<br>network.example/halvern<br>video.example/halvern
    </div>
  </section>

</div>
</body>
</html>
```